Business Card Design Project for Investment Fund

Orvanel Asset Partners is an emerging wealth management firm based in New Jersey. It offers superior investment returns to high net worth individuals and institutions by finding undervalued assets.
We recently selected a company logo which was inspired by the Tucana constellation. Beta Tucanae is a group of six stars, containing star cluster 47 Tucanae, rated the second brightest object in the sky.
Now we need a business card design. Since we are an investment firm, the design should project a sense of stability, growth and professionalism. The owner is interested in something simple yet striking, which of course is consistent with the logo.
Target Market(s)
Wealthy individuals, probably middle aged or older, in the US
Industry/Entity Type
Investment

```html
<!DOCTYPE html>
<html lang="en">
<head>
<meta charset="utf-8">
<title>Orvanel Asset Partners — Business Card</title>
<link rel="stylesheet" href="https://fonts.googleapis.com/css2?family=Open+Sans:wght@400;600;700&display=swap">
<style>
  :root {
    --page-bg: #ece9e4;
    --card-white: #ffffff;
    --ink-dark: #3a4044;
    --ink-grey: #5d6266;
    --strip-dark: #2f3437;
    --navy-deep: #0a0f6e;
    --navy-mid: #1a2a9c;
    --panel-top: #2d4aa8;
    --panel-bottom: #232a78;
    --text-light: #ffffff;
    --glow: rgba(170, 190, 255, 0.55);
  }
  * { box-sizing: border-box; margin: 0; padding: 0; }
  html, body {
    width: 1200px; height: 722px; overflow: hidden;
    background: var(--page-bg);
    font-family: "Open Sans", Arial, sans-serif;
  }
  .canvas {
    position: relative; width: 1200px; height: 722px;
    display: flex; align-items: center; justify-content: center; gap: 50px;
  }
  .card {
    position: relative; width: 540px; height: 310px;
    border-radius: 26px; overflow: hidden;
    box-shadow: 0 6px 18px rgba(0,0,0,0.18);
  }

  /* Front */
  .card-front { background: var(--card-white); }
  .brand {
    position: absolute; left: 40px; top: 78px; width: 210px;
    display: flex; flex-direction: column; align-items: center;
  }
  .brand-mark {
    width: 78px; height: 78px; border-radius: 16px;
    background: linear-gradient(160deg, var(--navy-mid), var(--navy-deep));
  }
  .brand-name {
    margin-top: 16px; text-align: center;
    font-size: 21px; font-weight: 700; line-height: 1.2;
    color: var(--ink-dark); letter-spacing: 0.5px;
  }
  .url-strip {
    position: absolute; left: 262px; top: 36px; width: 28px; height: 236px;
    background: linear-gradient(to bottom, var(--strip-dark), #4a5054);
    display: flex; align-items: center; justify-content: center;
  }
  .url-strip span {
    transform: rotate(-90deg); white-space: nowrap;
    color: var(--text-light); font-size: 13px; font-weight: 700; letter-spacing: 0.3px;
  }
  .contact-panel {
    position: absolute; left: 298px; top: 36px; right: 0; height: 236px;
    background: linear-gradient(to bottom, var(--panel-top), var(--panel-bottom));
    color: var(--text-light); padding: 30px 18px 0 20px;
  }
  .person { font-size: 16px; font-weight: 700; }
  .person .role { font-size: 11px; font-weight: 400; letter-spacing: 1.5px; }
  .contact-list { list-style: none; margin-top: 16px; }
  .contact-list li {
    display: flex; align-items: flex-start; gap: 8px;
    font-size: 12.5px; line-height: 1.35; margin-bottom: 8px;
  }
  .contact-list li.address { margin-top: 16px; }
  .contact-list svg { flex: none; width: 13px; height: 13px; margin-top: 2px; }

  /* Back */
  .card-back {
    background: radial-gradient(ellipse at 50% 42%, var(--navy-mid) 0%, var(--navy-deep) 70%);
    display: flex; flex-direction: column; align-items: center;
  }
  .back-mark {
    margin-top: 44px; width: 150px; height: 150px; border-radius: 26px;
    background: linear-gradient(160deg, #2a4ac0, var(--navy-mid));
    box-shadow: 0 0 36px 10px var(--glow);
  }
  .back-name {
    margin-top: 26px; font-size: 18px; font-weight: 600;
    color: var(--text-light); letter-spacing: 1px;
  }
  .back-url {
    margin-top: 8px; font-size: 14px; color: var(--text-light); letter-spacing: 2px;
  }
</style>
</head>
<body>
<main class="canvas">
  <section class="card card-front">
    <div class="brand">
      <div class="brand-mark"></div>
      <p class="brand-name">Orvanel Asset Partners</p>
    </div>
    <div class="url-strip"><span>www.orvanelasset.com</span></div>
    <div class="contact-panel">
      <p class="person">Daniel Hartley<span class="role">, CEO</span></p>
      <ul class="contact-list">
        <li>
          <svg viewBox="0 0 16 16"><circle cx="8" cy="8" r="7" fill="none" stroke="#fff" stroke-width="1.3"/><path d="M5.5 4.5l1.5 0 .6 2-1 .8a5 5 0 0 0 2.1 2.1l.8-1 2 .6v1.5c-3.5.3-6.3-2.5-6-6z" fill="#fff"/></svg>
          212-555-0148
        </li>
        <li>
          <svg viewBox="0 0 16 16"><rect x="1.5" y="4" width="13" height="9" rx="1" fill="#fff"/><path d="M1.5 4.5l6.5 4.5 6.5-4.5" fill="none" stroke="#2d4aa8" stroke-width="1.2"/></svg>
          dhartley@orvanelasset.com
        </li>
        <li class="address">
          <svg viewBox="0 0 16 16"><path d="M8 1a5 5 0 0 0-5 5c0 3.5 5 9 5 9s5-5.5 5-9a5 5 0 0 0-5-5z" fill="#fff"/><circle cx="8" cy="6" r="1.8" fill="#2d4aa8"/></svg>
          <span>210 Mercer Ave.<br>Jersey City, NJ 07302</span>
        </li>
      </ul>
    </div>
  </section>

  <section class="card card-back">
    <div class="back-mark"></div>
    <p class="back-name">Orvanel Asset Partners</p>
    <p class="back-url">www.orvanelasset.com</p>
  </section>
</main>
</body>
</html>
```